Moder Business Card Design for Renewables Business

Need a business card design for my business. We collect & repurpose spent coffee ground from cafes. The cards will be made from recycled paper. Needs to fit our corporate colour scheme of white, green & brown (see logo for colour codes). Eco friendly, modern, intresting & eye catching.
This card needs to convey the message of the business and fit into its mantra of eco-friendly, sustainable etc.

Target Market(s)

Cafe Owners, Coffee Drinkers, Recycling Companies, Farmers

Industry/Entity Type

Recycling

Contact Information for Business Card

Name; Peter Halloran
Phone; 0412 386 527
e-mail; info@lumatrove.com.au
website; www.lumatrove.com.au

Font styles to use
Sans Serif
Script

Colors

Designer to choose colors to be used in the design.

Requirements
Must have
• FRONT;
• Logo, Name (Peter Halloran), phone number, e-mail address, website
• BACK;
• On the back in cursive text; 'GOOD GROUNDS FOR A GREENER DAY'
• Small facebook & Instagram logos with text 'Lumatrove'
Should not have
• messy design

```html
<!DOCTYPE html>
<html lang="en">
<head>
<meta charset="utf-8">
<title>Lumatrove Business Card</title>
<link href="https://fonts.googleapis.com/css2?family=Montserrat:wght@500;600;700&family=Dancing+Script:wght@600&display=swap" rel="stylesheet">
<style>
  :root {
    --canvas-bg: #ececee;
    --leaf-green: #2e7b1e;
    --leaf-green-dark: #256817;
    --fresh-green: #6cae3c;
    --bean-brown: #6b3019;
    --paper: #dedddb;
    --white: #ffffff;
  }
  * { margin: 0; padding: 0; box-sizing: border-box; }
  html, body {
    width: 1200px; height: 800px; overflow: hidden;
    background: var(--canvas-bg);
    font-family: "Montserrat", Arial, sans-serif;
  }
  .stage {
    position: relative; width: 1200px; height: 800px;
    display: flex; align-items: center; justify-content: center; gap: 48px;
  }
  .card {
    position: relative; width: 532px; height: 304px;
    border-radius: 4px;
    box-shadow: 0 10px 28px rgba(0,0,0,0.18), 0 2px 4px rgba(0,0,0,0.12);
    display: flex; flex-direction: column; align-items: center; justify-content: center;
    text-align: center;
  }
  /* Back side */
  .card--back {
    background: radial-gradient(circle at 45% 40%, var(--leaf-green) 0%, var(--leaf-green-dark) 100%);
  }
  .brand-mark {
    width: 108px; height: 108px; border-radius: 50%;
    border: 4px solid var(--bean-brown);
    margin-bottom: 14px;
  }
  .card--back .brand-mark { border-color: var(--white); }
  .brand-name {
    font-weight: 600; font-size: 30px; letter-spacing: 2px; line-height: 1;
  }
  .card--back .brand-name { color: var(--white); }
  .tagline {
    font-family: "Dancing Script", cursive;
    font-size: 21px; color: var(--bean-brown); margin-top: 6px;
  }
  .social {
    display: flex; align-items: center; gap: 8px; margin-top: 16px;
    color: var(--white); font-size: 14px; font-weight: 500; letter-spacing: 0.5px;
  }
  .social__square { width: 14px; height: 14px; background: var(--white); border-radius: 2px; }

  /* Front side */
  .card--front { background: var(--paper); }
  .card--front .brand-mark { width: 92px; height: 92px; border-color: var(--fresh-green); margin-bottom: 10px; }
  .card--front .brand-name { color: var(--fresh-green); font-size: 26px; }
  .person-name {
    margin-top: 20px; color: var(--bean-brown);
    font-weight: 700; font-size: 20px; letter-spacing: 0.5px; text-transform: uppercase;
  }
  .rule { width: 56px; height: 2px; background: var(--bean-brown); margin: 8px 0 12px; }
  .contact-row {
    display: flex; gap: 22px; color: var(--bean-brown); font-size: 14px; font-weight: 500;
  }
  .contact-item { display: flex; align-items: center; gap: 6px; }
  .contact-item svg { width: 14px; height: 14px; fill: var(--fresh-green); }
  .website {
    margin-top: 10px; color: var(--fresh-green);
    font-size: 14px; font-weight: 600; letter-spacing: 4px;
  }
</style>
</head>
<body>
<main class="stage">
  <section class="card card--back" aria-label="Card back">
    <div class="brand-mark"></div>
    <div class="brand-name">LUMATROVE</div>
    <div class="tagline">Good grounds for a greener day</div>
    <div class="social">
      <span class="social__square"></span>
      <span>/Lumatrove</span>
    </div>
  </section>

  <section class="card card--front" aria-label="Card front">
    <div class="brand-mark"></div>
    <div class="brand-name">LUMATROVE</div>
    <div class="person-name">Peter Halloran</div>
    <div class="rule"></div>
    <div class="contact-row">
      <span class="contact-item">
        <svg viewBox="0 0 24 24" aria-hidden="true"><path d="M6.6 10.8a15.1 15.1 0 0 0 6.6 6.6l2.2-2.2a1 1 0 0 1 1-.25 11.4 11.4 0 0 0 3.6.57 1 1 0 0 1 1 1V20a1 1 0 0 1-1 1A17 17 0 0 1 3 4a1 1 0 0 1 1-1h3.5a1 1 0 0 1 1 1c0 1.25.2 2.45.57 3.57a1 1 0 0 1-.25 1z"/></svg>
        0412 386 527
      </span>
      <span class="contact-item">
        <svg viewBox="0 0 24 24" aria-hidden="true"><path d="M2 5h20v14H2z M2 5l10 7 10-7" /></svg>
        info@lumatrove.com.au
      </span>
    </div>
    <div class="website">www.lumatrove.com.au</div>
  </section>
</main>
</body>
</html>
```